Business Cards and Stationary for Dental Office
Modern dental office
I need double sided standard sized Business Card [3.5" x 2"]
You can use either the same font, or change it up--as long as it looks good
Bright & Fun-filled
Folasade Ikeribe DDS
Dr.
5128 Marlow Ave
Suite 210
Cedarvale, MD 21000
TBD
Info@mycedarlinedental.com
www.mycedarlinedental.com
The phone number is tbd
Please note this as I will ask for it to be added at a later date. Thanks
This is my logo in AI

```html
<!DOCTYPE html>
<html lang="en">
<head>
<meta charset="utf-8">
<title>Cedarline Dental Care – Business Card</title>
<link rel="stylesheet" href="https://fonts.googleapis.com/css2?family=Cormorant+Garamond:wght@500&family=Lato:wght@400;700&display=swap">
<style>
  :root {
    --page: #e4e5e6;
    --card: #ffffff;
    --green: #8cc9a0;
    --green-dark: #5fae7c;
    --grey: #8a8c8e;
    --grey-light: #c9cacb;
    --ink: #6d6f71;
  }
  * { box-sizing: border-box; margin: 0; padding: 0; }
  html, body { width: 1200px; height: 987px; overflow: hidden; }
  body {
    background: var(--page);
    font-family: "Lato", Arial, sans-serif;
    color: var(--ink);
    position: relative;
  }
  .card {
    position: absolute;
    left: 250px;
    width: 700px;
    height: 400px;
    background: var(--card);
    border-radius: 22px;
    overflow: hidden;
    box-shadow: 0 10px 28px rgba(0,0,0,0.12);
  }
  .card--front { top: 60px; }
  .card--back { top: 527px; }

  .wordmark {
    font-family: "Cormorant Garamond", Georgia, serif;
    font-weight: 500;
    color: var(--grey);
    letter-spacing: 0.06em;
    text-transform: uppercase;
    line-height: 1.1;
  }
  .wordmark-dot {
    border-radius: 50%;
    background: var(--green);
  }

  /* front */
  .front-brand {
    position: absolute; left: 0; right: 0; top: 130px;
    display: flex; flex-direction: column; align-items: center; gap: 16px;
  }
  .front-brand .wordmark-dot { width: 56px; height: 56px; }
  .front-brand .wordmark { font-size: 30px; }
  .front-web {
    position: absolute; left: 0; right: 0; top: 268px;
    text-align: center; font-size: 11px; letter-spacing: 0.32em;
    text-transform: uppercase; color: var(--grey);
  }

  /* back */
  .back-shapes { position: absolute; inset: 0; }
  .back-brand {
    position: absolute; left: 40px; top: 108px;
    display: flex; flex-direction: column; align-items: flex-start; gap: 10px;
  }
  .back-brand .wordmark-dot { width: 38px; height: 38px; }
  .back-brand .wordmark { font-size: 27px; }
  .tagline { font-size: 10px; color: var(--green-dark); letter-spacing: 0.08em; }
  .person { position: absolute; left: 40px; top: 232px; }
  .person-name {
    font-size: 13px; color: var(--green-dark); letter-spacing: 0.14em;
    text-transform: uppercase; font-weight: 700;
  }
  .person-title { font-size: 11px; letter-spacing: 0.14em; text-transform: uppercase; margin-top: 5px; }
  .contact {
    position: absolute; left: 380px; top: 266px;
    list-style: none; font-size: 11px; line-height: 1.55;
  }
  .contact li { display: flex; align-items: center; gap: 8px; white-space: nowrap; }
  .contact svg { width: 10px; height: 10px; fill: var(--green-dark); flex: none; }
  .contact .indent { padding-left: 18px; }
</style>
</head>
<body>

<section class="card card--front" aria-label="Business card front">
  <div class="front-brand">
    <span class="wordmark-dot"></span>
    <span class="wordmark">Cedarline Dental Care</span>
  </div>
  <p class="front-web">www.mycedarlinedental.com</p>
</section>

<section class="card card--back" aria-label="Business card back">
  <svg class="back-shapes" viewBox="0 0 700 400" preserveAspectRatio="none" aria-hidden="true">
    <defs>
      <linearGradient id="greyBand" x1="0" y1="0" x2="1" y2="0">
        <stop offset="0" stop-color="#d6d7d8"/>
        <stop offset="1" stop-color="#9d9fa1"/>
      </linearGradient>
    </defs>
    <path d="M700 0 L700 400 L560 400 C 640 300 650 140 560 0 Z" fill="url(#greyBand)"/>
    <path d="M0 0 L700 0 L700 30 C 520 20 300 30 0 70 Z" fill="#f1f2f2"/>
    <path d="M0 62 C 250 18 480 8 700 26 L700 40 C 480 22 250 34 0 82 Z" fill="var(--green)"/>
    <path d="M0 86 C 250 42 480 34 700 48 L700 56 C 480 44 250 54 0 96 Z" fill="var(--grey-light)"/>
  </svg>

  <div class="back-brand">
    <span class="wordmark-dot"></span>
    <span class="wordmark">Cedarline Dental Care</span>
    <span class="tagline">Gentle care for healthy, happy smiles</span>
  </div>

  <div class="person">
    <p class="person-name">Folasade Ikeribe DDS</p>
    <p class="person-title">Dr. · Dentist</p>
  </div>

  <ul class="contact">
    <li><svg viewBox="0 0 10 10"><path d="M5 0a3.5 3.5 0 0 0-3.5 3.5C1.5 6 5 10 5 10s3.5-4 3.5-6.5A3.5 3.5 0 0 0 5 0zm0 5a1.5 1.5 0 1 1 0-3 1.5 1.5 0 0 1 0 3z"/></svg>5128 Marlow Ave, Suite 210</li>
    <li class="indent">Cedarvale, MD 21000</li>
    <li><svg viewBox="0 0 10 10"><path d="M2 0h2l1 2.5-1.3 1a6 6 0 0 0 2.8 2.8l1-1.3L10 6v2a2 2 0 0 1-2 2C3.6 10 0 6.4 0 2a2 2 0 0 1 2-2z"/></svg>Phone: TBD</li>
    <li><svg viewBox="0 0 10 10"><rect x="1" y="2" width="8" height="6" rx="1"/></svg>Fax: TBD</li>
    <li><svg viewBox="0 0 10 10"><path d="M0 2h10v6H0z M0 2l5 3.5L10 2"/></svg>Info@mycedarlinedental.com</li>
    <li><svg viewBox="0 0 10 10"><circle cx="5" cy="5" r="4.5"/></svg>www.mycedarlinedental.com</li>
  </ul>
</section>

</body>
</html>
```